Presentation Folder

We are looking for a presentation folder design that will allow us to bring our proposals/quotes to clients and leave with them. The front cover should have our logo as well as show some of the products we sell: IT Networking equipment, WiFi, Servers/Storage.
Inside flap has an area for our business cards.

Target Market(s)

Mid Sized Businesses and Private Education. Business to Business. IT Directors. Ages 30 to 50. College Educated. Southern California

Industry/Entity Type

Business

Logo Text

Requirements
Must have
• Our Logo
Complimentary color schemes to our logo.
Should be Professional.

```html
<!DOCTYPE html>
<html lang="en">
<head>
<meta charset="utf-8">
<title>Halsten IT — Presentation Folder</title>
<link rel="stylesheet" href="https://fonts.googleapis.com/css2?family=Raleway:wght@300;400&display=swap">
<style>
  :root {
    --canvas-bg: #eeeeee;
    --flap-grey: #a0a0a0;
    --panel-grey: #a2a2a2;
    --photo-dark: #1e1f21;
    --accent-blue: #00acd8;
    --navy: #2d4670;
    --white: #ffffff;
    --logo-grey: #7d7d7d;
    --address-grey: #a9a9a9;
  }
  * { margin: 0; padding: 0; box-sizing: border-box; }
  html, body {
    width: 1200px; height: 916px; overflow: hidden;
    background: var(--canvas-bg);
    font-family: "Raleway", sans-serif;
  }
  .folder { position: relative; width: 1200px; height: 916px; }
  .dieline { position: absolute; inset: 0; }
  .cover { position: absolute; left: 175px; top: 14px; width: 1010px; height: 694px; }
  .back-panel {
    position: absolute; left: 0; top: 0; width: 504px; height: 509px;
    background: var(--panel-grey);
  }
  .tagline {
    position: absolute; left: 0; width: 504px; top: 479px;
    text-align: center; color: var(--white);
    font-weight: 400; font-size: 13.5px; letter-spacing: 0.2px;
  }
  .product-photo {
    position: absolute; left: 504px; top: 0; width: 506px; height: 509px;
    background:
      radial-gradient(ellipse 45% 55% at 52% 55%, rgba(90,170,90,0.55), rgba(60,110,150,0.25) 55%, transparent 80%),
      radial-gradient(ellipse 60% 45% at 55% 25%, rgba(220,230,240,0.25), transparent 75%),
      var(--photo-dark);
  }
  .accent-band {
    position: absolute; left: 0; top: 509px; width: 1010px; height: 14px;
    background: var(--accent-blue);
  }
  .info-strip {
    position: absolute; left: 0; top: 523px; width: 1010px; height: 157px;
    background: var(--white);
  }
  .address {
    position: absolute; left: 0; width: 504px; top: 60px;
    text-align: center; color: var(--address-grey);
    font-weight: 300; font-size: 12px; line-height: 13px;
  }
  .brand {
    position: absolute; left: 676px; top: 52px;
    display: flex; align-items: center; gap: 12px;
  }
  .brand-mark { width: 14px; height: 14px; background: var(--accent-blue); }
  .brand-name {
    color: var(--logo-grey); font-weight: 300; font-size: 47px;
    letter-spacing: 0.5px; line-height: 1;
  }
  .gradient-band {
    position: absolute; left: 0; top: 680px; width: 1010px; height: 14px;
    background: linear-gradient(90deg, var(--navy), var(--accent-blue) 50%, var(--navy));
  }
</style>
</head>
<body>
<div class="folder">
  <svg class="dieline" width="1200" height="916" viewBox="0 0 1200 916" aria-hidden="true">
    <path class="side-flap" fill="var(--flap-grey)"
      d="M175 196 L150 198 Q112 208 100 272 L14 652 L175 708 Z"/>
    <path class="pocket-flap" fill="var(--flap-grey)"
      d="M175 708 L224 773 Q196 782 198 818 Q203 862 246 866 Q262 866 275 858 L308 901 Q520 890 668 796 L668 708 Z"/>
  </svg>

  <div class="cover">
    <div class="back-panel">
      <p class="tagline">Get Connected. Anywhere. Anytime.</p>
    </div>
    <div class="product-photo" role="img" aria-label="Photograph of a bundle of colourful fibre-optic cables fanning out with glowing tips on a dark background"></div>
    <div class="accent-band"></div>
    <div class="info-strip">
      <p class="address">
        Corporate Headquarters<br>
        2740 Harbor Way, Suite 310<br>
        Bayview, CA 92800<br>
        555-014-2273
      </p>
      <div class="brand">
        <span class="brand-mark"></span>
        <span class="brand-name">HALSTEN IT</span>
      </div>
    </div>
    <div class="gradient-band"></div>
  </div>
</div>
</body>
</html>
```